Web Design - Personal Item Tags Portal

web page designs need to be created for a new company that provides item tracking tags and lets users register and report stolen/found items.
The theme of the designs needs to be energetic and convey a sense of freedom and adventure - where the user does not have to worry about their items since they have all been "tagged".
the client likes parts of the site at: http://www.brisklayouts.example/
they like:
1. slider images at top of pages. large slider on front page. fixed smaller height picture on internal pages
2. fixed company message on left-hand-side
3. My Account button to be clear and stand out

other comments:
clean, simple
• brand focused
• will have clear call to actions
• will include a description of what and why
• will appeal to both males and females

sections that the website will have are:
Home
About Us
How it works
Why
Case Studies
Uses and Applications
Shop
Contact Us

please create 2 designs : 1 home page, 1 internal page

Final winner will also require HTML slicing to be done.
Updates

hi, i have now updated the images so they work. sorry!

Hi, looking at all the designs that are coming in, alot of them are great. Designers need to remember to make the register for an account button more prominent. Also, there should be a "report found" and "report lost" buttons on the front-page and should be prominent as well.

Thanks

Hi, the customer has come back with a few comments and modifications for the designs, if you are able to make some tweaks to your submissions, that will be great:

The client would like the designs to be modified to highlight 3 main actions:
1. Log In/Register
2. Find an Owner
3. Lost an Item

The home page shouldnt be too content heavy in terms of text, it should only have major highlight points of what the system does (the 3 points listed above). the inner page designs are OK to have more text though.

i will also upload some notes from the customer that can be used as a guide and also include the design styles which the customer likes (but is not entirely happy with).

uploaded image files (3) with customer feedback comments

Industry/Entity Type

It Company

```html
<!DOCTYPE html>
<html lang="en">
<head>
<meta charset="utf-8">
<title>TrailMark – About us</title>
<link rel="stylesheet" href="https://fonts.googleapis.com/css2?family=Questrial&family=Oswald:wght@200&family=Arimo:wght@400;700&display=swap">
<style>
  :root {
    --black: #000000;
    --brand-blue: #0c5a8a;
    --nav-blue: #0a5686;
    --title-blue: #1d6c9e;
    --panel: rgba(255, 255, 255, 0.74);
    --text: #111111;
    --footer-text: #c4c4c4;
    --footer-muted: #8a8a8a;
    --field: #0e3d5f;
    --social: #175f90;
    --line: #2e6e9c;
  }
  * { box-sizing: border-box; margin: 0; padding: 0; }
  html, body { width: 1200px; height: 1038px; overflow: hidden; background: var(--black); }
  body { position: relative; font-family: "Arimo", Arial, sans-serif; color: var(--text); }

  /* Header */
  .site-header { position: absolute; left: 0; top: 0; width: 1200px; height: 153px; background: var(--black); }
  .brand-badge {
    position: absolute; left: 0; top: 0; width: 190px; height: 153px;
    background: radial-gradient(circle at 50% 45%, #ffffff 0%, #9fd4ff 18%, #2d7fc4 42%, #0b2f55 75%, #041526 100%);
  }
  .brand-badge .mark-dot {
    position: absolute; left: 65px; top: 46px; width: 58px; height: 58px;
    border-radius: 50%; background: var(--black);
  }
  .brand-name {
    position: absolute; left: 214px; top: 24px;
    font-family: "Questrial", sans-serif; font-size: 50px; color: #ffffff; letter-spacing: 0.5px;
  }
  .tagline {
    position: absolute; left: 440px; top: 50px;
    font-family: "Questrial", sans-serif; font-size: 20px; color: #ffffff;
  }
  .main-nav {
    position: absolute; left: 184px; top: 110px; width: 1016px; height: 43px;
    background: var(--nav-blue); display: flex; align-items: stretch;
  }
  .main-nav a {
    font-family: "Questrial", sans-serif; font-size: 19.5px; color: #ffffff; text-decoration: none;
    display: flex; align-items: center; padding: 0 14px;
  }
  .main-nav a.home { font-weight: 700; padding-left: 14px; }
  .main-nav a.current { background: #eeeeee; color: var(--title-blue); font-weight: 700; margin: 0 8px; padding: 0 15px; }

  /* Hero */
  .hero { position: absolute; left: 0; top: 153px; width: 1200px; height: 612px; }
  .hero-photo {
    position: absolute; inset: 0;
    background:
      linear-gradient(90deg, rgba(0,0,0,0) 0%, rgba(0,0,0,0) 68%, rgba(150,120,90,0.9) 74%, #8a7562 85%, #6e5c4c 100%),
      linear-gradient(180deg, #8aa7b6 0%, #b9b7a0 35%, #e4cd8c 65%, #f6e7b0 85%, #e9cf86 100%);
  }
  .about-panel {
    position: absolute; left: 28px; top: 32px; width: 775px; height: 536px;
    background: var(--panel); border-radius: 10px; padding: 30px 44px 0 42px;
  }
  .about-panel h1 {
    font-family: "Questrial", sans-serif; font-weight: 400; font-size: 43px;
    color: var(--title-blue); line-height: 1; margin-bottom: 15px;
  }
  .about-panel p { font-size: 17px; line-height: 20.5px; margin-bottom: 20.5px; }
  .slider-dots { position: absolute; left: 1032px; top: 729px; display: flex; gap: 12.5px; }
  .slider-dots span { width: 17px; height: 17px; border-radius: 50%; background: var(--black); }
  .slider-dots span.active { background: #ffffff; }
  .hero-rule { position: absolute; left: 0; top: 765px; width: 1200px; height: 2px; background: var(--line); }

  /* Footer */
  .site-footer { position: absolute; left: 0; top: 767px; width: 1200px; height: 271px; }
  .footer-heading {
    position: absolute; top: 49px;
    font-family: "Questrial", sans-serif; font-weight: 700; font-size: 20px;
    letter-spacing: 1px; color: #e6e6e6; text-transform: uppercase;
  }
  .footer-links { position: absolute; top: 95px; list-style: none; }
  .footer-links li { font-size: 14.5px; line-height: 17.6px; color: var(--footer-text); }
  .social { position: absolute; left: 532px; top: 84px; display: flex; gap: 10px; }
  .social span { width: 34px; height: 34px; border-radius: 50%; background: var(--social); }
  .newsletter-label { position: absolute; left: 532px; top: 134px; font-size: 13px; color: var(--footer-text); }
  .newsletter-field {
    position: absolute; left: 529px; top: 160px; width: 226px; height: 33px;
    border-radius: 17px; background: var(--field); color: #dfe8ef;
    font-size: 13px; line-height: 33px; padding-left: 18px;
  }
  .subscribe { position: absolute; left: 535px; top: 206px; font-size: 13px; font-weight: 700; color: #a8a8a8; }
  .phone {
    position: absolute; left: 942px; top: 73px;
    font-family: "Oswald", sans-serif; font-weight: 200; font-size: 41px; color: var(--footer-muted);
  }
  .contact-dot { position: absolute; left: 1008px; top: 134px; width: 32px; height: 32px; border-radius: 50%; background: #9a9a9a; }
  .copyright {
    position: absolute; left: 924px; top: 178px; width: 200px; text-align: center;
    font-size: 14.5px; line-height: 18px; color: var(--footer-text);
  }
</style>
</head>
<body>
  <header class="site-header">
    <div class="brand-badge"><span class="mark-dot"></span></div>
    <div class="brand-name">TrailMark</div>
    <div class="tagline">. . . explore freely</div>
    <nav class="main-nav">
      <a class="home">Home</a>
      <a class="current">About us</a>
      <a>How it works</a>
      <a>Why</a>
      <a>Case Studies</a>
      <a>Uses and Applications</a>
      <a>Shop</a>
      <a>Contact Us</a>
    </nav>
  </header>

  <section class="hero">
    <div class="hero-photo" role="img" aria-label="Climber hanging from a sunlit rock face against a golden sky"></div>
    <article class="about-panel">
      <h1>ABOUT US</h1>
      <p>Lorem ipsum dolor sit amet, consectetuer adipiscing elit, sed diam nonummy nibh euismod tincidunt ut laoreet dolore magna aliquam erat volutpat. Ut wisi enim ad minim veniam, quis nostrud exerci tation ullamcorper suscipit lobortis nisl ut aliquip ex ea commodo consequat.</p>
      <p>Duis autem vel eum iriure dolor in hendrerit in vulputate velit esse molestie consequat, vel illum dolore eu feugiat nulla facilisis at vero eros et accumsan et iusto odio dignissim qui blandit praesent luptatum zzril delenit augue duis dolore te feugait nulla facilisi. Nam liber tempor cum soluta nobis eleifend option congue nihil imperdiet doming id quod mazim placerat facer possim assum. Typi non habent claritatem insitam; est usus legentis in iis qui facit eorum claritatem. Investigationes demonstraverunt lectores legere me lius quod ii legunt saepius.</p>
      <p>Claritas est etiam processus dynamicus, qui sequitur mutationem consuetudium lectorum. Mirum est notare quam littera gothica, quam nunc putamus parum claram, anteposuerit litterarum formas humanitatis per seacula quarta decima et quinta decima. Eodem modo typi, qui nunc nobis videntur parum clari, fiant sollemnes in futurum.</p>
    </article>
  </section>
  <div class="slider-dots"><span></span><span class="active"></span><span></span><span></span><span></span></div>
  <div class="hero-rule"></div>

  <footer class="site-footer">
    <h2 class="footer-heading" style="left:50px">Navigation</h2>
    <ul class="footer-links" style="left:50px">
      <li>Home</li><li>About us</li><li>How it works</li><li>Why</li>
      <li>Case Studies</li><li>Uses and Applications</li><li>Shop</li>
    </ul>
    <ul class="footer-links" style="left:249px">
      <li>Sitemap</li><li>Report Found</li><li>Report Lost</li><li>Register an Account</li>
      <li>Contact Us</li><li>Terms of Use</li><li>Privacy Policy</li>
    </ul>

    <h2 class="footer-heading" style="left:533px">Get Connected</h2>
    <div class="social"><span></span><span></span><span></span><span></span><span></span></div>
    <div class="newsletter-label">Subscribe to our newsletter</div>
    <div class="newsletter-field">enter email address</div>
    <div class="subscribe">subscribe now &#10148;</div>

    <h2 class="footer-heading" style="left:945px">Contact Us</h2>
    <div class="phone">0987 654 321</div>
    <span class="contact-dot"></span>
    <div class="copyright">© TrailMark 2013.<br>All rights reserved.</div>
  </footer>
</body>
</html>
```